Business Card Design

I am a Accredited RiverPath Officiant(r) (this title requires the Registered Trademark come after it). I am also A Non-Denominational Minister. My minister title is important, but not my primary focus. My primary line of business is custom weddings. I also offer other ceremonies across the range of life experiences. Right now the back of my card lists the other ceremonies I create and lead. I have a logo that was just developed and I want to use my logo for my cards. I have the logo in every possible format, color black/white also broken up with just the graphic of just the name. I can send other formats if needed. You can see info about my wedding work at www.lanternrites.com. My physical address is less important than my email and phone number. My secondary line of business is personalized funerals and memorials. The challenge is I don't want to have more than one card, but I want to separate weddings and funerals. Thinking funerals needs to go on the back. I hate my funeral website name(www.gentlepartingsne.com) but it might be important to use it.
Information on back of card currently says:
Specializing in Couples Centered Custom Wedding Ceremonies.
Addition Services: Creating ways to express the meaningful moments of your life, in your on way: Baby Welcoming's and Naming's, Mother/Father Parent Passages for birth and adoption, Engagement and Vow Renewals, New Home Dedications, Creative Business Ribbon Cuttings, Ceremonies of Transition-moving, home sale, business closing, career change, Croning. Ceremonies of Healing-divorce, job loss, recovery, rededication, Transgender Naming Ceremonies, Coming Out Ceremonies. Ceremonies to Celebrate life and honor death-custom funeral and personalized life memorials. Ceremony writing services also available.

Target Market(s)

95% of my business is wedding clients both gay and straight.Also do custom funerals.I also do other ceremony want to use only 1 card for all products

Industry/Entity Type

Wedding

Contact Information for Business Card

Marla J. Penwick, Non-Denominational Minister
Accredited River-Path Officiant(r)
Lantern Rites
217 Fenwick Rd. Wrenfield, VT 05871
5554173926
www.lanternrites.com
tag line on front Heartfelt Custom Created Ceremonies

```html
<!DOCTYPE html>
<html lang="en">
<head>
<meta charset="utf-8">
<title>Lantern Rites — Business Card</title>
<link href="https://fonts.googleapis.com/css2?family=Source+Sans+3:wght@400;600;700&display=swap" rel="stylesheet">
<style>
  :root{
    --bg:#e4e5e4;
    --card-white:#ffffff;
    --green:#1d7a55;
    --green-deep:#0c4a30;
    --green-mid:#1e6a44;
    --red:#b0241f;
    --ink:#2b2b2b;
    --grey:#6f6f6f;
    --cream:#e9ecd9;
    --lime:#b6cf2c;
  }
  *{box-sizing:border-box;margin:0;padding:0}
  html,body{width:1200px;height:1000px;overflow:hidden}
  body{background:var(--bg);font-family:"Source Sans 3",Arial,sans-serif;position:relative}

  .card{position:absolute;left:250px;width:700px;height:400px;overflow:hidden;box-shadow:0 6px 18px rgba(0,0,0,.18)}
  .card--back{top:60px;background:radial-gradient(ellipse at 50% 55%,#2c7f52 0%,var(--green-mid) 45%,var(--green-deep) 100%);color:var(--cream)}
  .card--front{top:540px;background:var(--card-white);color:var(--ink)}

  /* back */
  .back__rule{position:absolute;left:44px;top:42px;width:520px;height:3px;background:var(--lime)}
  .back__text{position:absolute;left:44px;top:62px;width:612px;font-size:17px;line-height:1.38;text-align:center}
  .back__text p{margin-bottom:16px}
  .back__text strong{font-weight:700;color:#f2f4e6}
  .back__web{position:absolute;right:22px;bottom:22px;padding:8px 22px;border-radius:10px;background:rgba(255,255,255,.08);border:1px solid rgba(255,255,255,.12);color:var(--lime);font-size:17px;font-weight:600}

  /* front */
  .front__tab{position:absolute;right:0;top:26px;width:26px;height:44px;background:var(--red)}
  .front__id{position:absolute;right:56px;top:34px;text-align:right}
  .front__name{font-size:26px;font-weight:700;color:var(--green)}
  .front__title{font-size:17px;color:var(--ink);line-height:1.25}
  .front__title--sub{color:var(--grey)}
  .front__contact{position:absolute;left:420px;top:176px;font-size:16px;line-height:1.35}
  .front__company{font-weight:700;font-size:17px}
  .front__addr{color:var(--grey);margin-bottom:12px}
  .front__line{display:flex;align-items:center;gap:7px}
  .front__line svg{flex:none}

  .brand{position:absolute;left:40px;top:126px;display:flex;align-items:center;gap:18px}
  .brand__dot{width:120px;height:120px;border-radius:50%;background:var(--green)}
  .brand__name{font-size:40px;font-weight:600;color:var(--red);line-height:1}

  .tagline{position:absolute;left:40px;top:266px;width:340px;height:28px;background:var(--green);color:#fff;font-size:17px;display:flex;align-items:center;justify-content:center}
  .specialty{position:absolute;left:58px;top:300px;font-size:17px;line-height:1.2}
  .specialty strong{font-weight:700}
  .front__web{position:absolute;left:0;bottom:0;width:330px;height:48px;background:var(--green);border-top-right-radius:14px;color:#fff;font-size:17px;display:flex;align-items:center;padding-left:40px}
</style>
</head>
<body>

<section class="card card--back" aria-label="Card back">
  <div class="back__rule"></div>
  <div class="back__text">
    <p><strong>Addition Services:</strong> Creating ways to express the meaningful moments of your life, in your own way: Baby Welcoming's and Naming's, Mother/Father Parent Passages for birth and adoption, Engagement and Vow Renewals, New Home Dedications, Creative Business Ribbon Cuttings, Ceremonies of Transition-moving, home sale, business closing, career change, Croning.</p>
    <p>Ceremonies of Healing-divorce, job loss, recovery, rededication, Transgender Naming Ceremonies, Coming Out Ceremonies.</p>
    <p>Ceremonies to Celebrate life and honor death-custom funeral and personalized life memorials. Ceremony writing services also available.</p>
  </div>
  <div class="back__web">www.lanternrites.com</div>
</section>

<section class="card card--front" aria-label="Card front">
  <div class="front__tab"></div>

  <div class="front__id">
    <div class="front__name">Marla J. Penwick</div>
    <div class="front__title">Accredited River-Path Officiant®</div>
    <div class="front__title front__title--sub">Non-Denominational Minister</div>
  </div>

  <div class="brand">
    <div class="brand__dot"></div>
    <div class="brand__name">Marla<br>Penwick</div>
  </div>

  <div class="tagline">Heartfelt Custom Created Ceremonies</div>
  <div class="specialty"><strong>Specializing in:</strong> Couples Centered<br>Custom Wedding Ceremonies.</div>

  <div class="front__contact">
    <div class="front__company">Lantern Rites</div>
    <div class="front__addr">217 Fenwick Rd. Wrenfield, VT</div>
    <div class="front__line">
      <svg width="14" height="10" viewBox="0 0 14 10"><rect x="0.5" y="0.5" width="13" height="9" fill="none" stroke="#1d7a55"/><path d="M0.5 0.5 L7 5.5 L13.5 0.5" fill="none" stroke="#1d7a55"/></svg>
      <span>marla@lanternrites.com</span>
    </div>
    <div class="front__line">
      <svg width="10" height="14" viewBox="0 0 10 14"><rect x="0.5" y="0.5" width="9" height="13" rx="2" fill="none" stroke="#1d7a55"/><circle cx="5" cy="11" r="1" fill="#1d7a55"/></svg>
      <span>05871 5554173926</span>
    </div>
  </div>

  <div class="front__web">www.lanternrites.com</div>
</section>

</body>
</html>
```